Website for new dental office

I am Dr. Calvin Merrow and am building a new dental practice. I specialize in general dentistry. I am young and have a higher end dental practice incorporating very new technologies and would like my website to reflect that. As many dental patients are older, the website must be very easy to navigate. I would like patients to be able to request appointments, and will eventually add on patient information forms (the health history, etc, that you normally fill out in the practice) from my practice management software, so leave an area for that.

Industry/Entity Type

Building

```html
<!DOCTYPE html>
<html lang="en">
<head>
<meta charset="utf-8">
<title>Merrow Dental</title>
<link href="https://fonts.googleapis.com/css2?family=Lato:wght@400;700&display=swap" rel="stylesheet">
<style>
:root{
  --brand:#1a5aa8;
  --hero:#0f58a6;
  --nav-top:#4479bd;
  --nav-bottom:#2b5b9f;
  --navy:#214d96;
  --footer:#224b92;
  --footer-dark:#183a70;
  --footer-text:#ffffff;
  --orange:#f57a1f;
  --orange-dark:#e0600e;
  --panel:#ddedf8;
  --text:#444;
  --heading:#333;
  --rule:#3b62a6;
}
*{box-sizing:border-box;margin:0;padding:0}
html,body{width:835px;height:1200px;overflow:hidden}
body{font-family:'Lato',sans-serif;background:#fff;position:relative;color:var(--text)}
.abs{position:absolute}
.header{left:0;top:0;width:835px;height:82px;background:#fff}
.logo{left:106px;top:26px;font-size:32px;font-weight:700;color:var(--brand);letter-spacing:-.3px}
.social{top:14px;width:20px;height:20px;border-radius:50%;background:#bdbdbd}
.phone{left:484px;top:43px;font-size:22px;color:var(--brand)}
.btn{background:linear-gradient(var(--orange),var(--orange-dark));color:#fff;font-weight:700;text-align:center;border-radius:2px}
.consult{left:649px;top:44px;width:71px;height:26px;font-size:8px;line-height:9px;padding-top:4px}
.nav{left:0;top:82px;width:835px;height:35px;background:linear-gradient(var(--nav-top),var(--nav-bottom));border-top:1px solid #a9bedc}
.nav span{position:absolute;top:10px;font-size:11.5px;color:#fff;transform:translateX(-50%)}
.hero{left:0;top:117px;width:835px;height:296px;background:var(--hero)}
.hero-photo{left:109px;top:134px;width:419px;height:251px;background:linear-gradient(135deg,#f1ebe6,#d9b7a0 45%,#b98a6c 70%,#e8e4e2)}
.booking{left:536px;top:134px;width:190px;height:251px;background:var(--panel)}
.booking-head{position:absolute;left:0;top:0;width:190px;height:30px;background:#1d4f98;color:#fff;font-size:12px;font-weight:700;padding:8px 0 0 36px}
.booking-head svg{position:absolute;left:17px;top:9px}
.field{position:absolute;left:17px;width:156px;height:22px;background:#fff;border:1px solid #cfdce8;font-size:8px;color:#8a96a3;padding:6px 0 0 7px}
.submit{position:absolute;left:58px;top:208px;width:49px;height:25px;font-size:10px;padding-top:7px}
.intro h1{font-size:17px;font-weight:400;color:var(--heading)}
.intro{left:110px;top:436px;width:355px}
.intro p{font-size:8.6px;line-height:13.6px;margin-top:10px}
.video{left:476px;top:438px;width:248px;height:189px;background:linear-gradient(135deg,#bfe0f3,#8cc3e6 50%,#e7d3c2)}
.video-bar{left:476px;top:606px;width:248px;height:21px;background:#1c1c1c;color:#ddd;font-size:7px}
.bar{background:var(--navy);color:#fff;font-size:8.6px;font-weight:700;padding:7px 0 0 10px;height:24px}
.treat{position:absolute;font-size:8.6px;color:#555}
.treat svg{position:absolute;left:0;top:-4px}
.treat span{margin-left:23px}
.link{font-size:8.6px;color:#333;text-decoration:underline}
.thumb{width:38px;height:39px;background:linear-gradient(#f3d0c4,#e7a39a 60%,#fff)}
.case{font-size:8.6px;color:#444;line-height:15px}
.case b{color:#1a5aa8}
.social-box{left:108px;top:826px;width:614px;height:76px;border:1px solid #ddd;background:#fff}
.fans{position:absolute;left:9px;top:10px;font-size:8.5px;color:#333}
.fans b{font-weight:400;color:#1a5aa8}
.fans i{display:inline-block;width:8px;height:8px;background:#1a5aa8;vertical-align:-1px;margin-right:4px}
.follow{position:absolute;right:16px;top:8px;font-size:8.5px;color:#1a3fc7;text-decoration:underline}
.avatar{position:absolute;top:27px;width:33px;height:33px;background:linear-gradient(#7d8794,#4a4f57)}
.footer{left:0;top:902px;width:835px;height:262px;background:var(--footer);color:var(--footer-text)}
.footer h2{position:absolute;top:22px;font-size:17px;font-weight:400}
.row{position:absolute;left:106px;width:155px;font-size:8.6px;color:var(--footer-text);display:flex;justify-content:space-between;padding-bottom:9px;border-bottom:1px solid var(--rule)}
.row.last{border-bottom:none}
.addr{position:absolute;left:321px;font-size:8.6px;color:var(--footer-text)}
.map{left:320px;top:1046px;width:142px;height:88px;background:linear-gradient(120deg,#e8eee0,#f2f0e6 55%,#a9c6e6 70%)}
.tips{left:533px;top:957px;font-size:8.6px;font-weight:700;color:var(--footer-text)}
.input{position:absolute;left:530px;width:191px;height:23px;background:#fff;font-size:8.6px;color:#888;padding:6px 0 0 8px}
.signup{left:650px;top:1110px;width:71px;height:25px;font-size:10.5px;padding-top:6px}
.bottom{left:0;top:1164px;width:835px;height:36px;background:var(--footer-dark)}
.bottom i{position:absolute;top:8px;width:20px;height:20px;border-radius:50%;background:#3c5a8c}
.copy{position:absolute;right:114px;top:14px;font-size:7.8px;color:#fff}
</style>
</head>
<body>
<div class="abs header"></div>
<div class="abs logo">Merrow Dental</div>
<div class="abs social" style="left:606px"></div>
<div class="abs social" style="left:638px"></div>
<div class="abs social" style="left:668px"></div>
<div class="abs social" style="left:700px"></div>
<div class="abs phone">(1800)555-0142</div>
<div class="abs btn consult">Request Free<br>Consultation</div>

<nav class="abs nav">
  <span style="left:139px">Home</span>
  <span style="left:199px">About Us</span>
  <span style="left:272px">Our Service</span>
  <span style="left:361px">Our Technology</span>
  <span style="left:450px">Dental Care</span>
  <span style="left:531px">Case Studies</span>
  <span style="left:617px">New Patients</span>
  <span style="left:690px">Contact</span>
</nav>

<div class="abs hero"></div>
<div class="abs hero-photo" role="img" aria-label="Smiling family of a father and three children"></div>
<form class="abs booking">
  <div class="booking-head">
    <svg width="12" height="11" viewBox="0 0 12 11"><rect x=".5" y="1.5" width="11" height="9" fill="none" stroke="#fff"/><rect x=".5" y="1.5" width="11" height="2.5" fill="#fff"/><path d="M3 5.5h2v1.5H3zM7 5.5h2v1.5H7zM3 8h2v1.5H3zM7 8h2v1.5H7z" fill="#fff"/></svg>
    Book An Appointment
  </div>
  <div class="field" style="top:49px">Select Service
    <svg style="position:absolute;right:0;top:0" width="22" height="20"><line x1="1" y1="3" x2="1" y2="17" stroke="#d5dfe9"/><path d="M9 9h6l-3 3z" fill="#2a66b5"/></svg>
  </div>
  <div class="field" style="top:78px">Full Name</div>
  <div class="field" style="top:107px">Email</div>
  <div class="field" style="top:136px">Phone</div>
  <div class="field" style="top:166px">Date of Appointment (required)</div>
  <div class="btn submit">Submit</div>
</form>

<section class="abs intro">
  <h1>Your Experience in Dentistry Begins Now!</h1>
  <p>It is a long established fact that a reader will be distracted by the readable content of a page when looking at its layout. The point of using Lorem Ipsum is that it has a more-or-less normal distribution of letters, as opposed to using 'Content here, content here', making it look like readable English.</p>
  <p>Lorem ipsum dolor sit amet, consectetur adipisicing elit, sed do eiusmod tempor incididunt ut labore et dolore magna aliqua. Ut enim ad minim veniam, quis nostrud exercitation ullamco laboris nisi ut aliquip ex ea commodo consequat.It is a long established fact that a reader will be distracted by the readable content of a page when looking at its layout. The point of using Lorem Ipsum is that it has a more-or-less normal distribution of letters, as opposed to using 'Content here, content here', making it look like readable English.</p>
</section>
<div class="abs video" role="img" aria-label="Dental practice video with dentist and smiling family"></div>
<div class="abs video-bar">
  <svg width="248" height="21" style="position:absolute;left:0;top:0">
    <rect x="0" y="0" width="248" height="3" fill="#555"/><rect x="0" y="0" width="40" height="3" fill="#e02323"/>
    <circle cx="21" cy="1.5" r="3" fill="#ddd"/>
    <path d="M12 8v8l7-4z" fill="#aaa"/>
    <path d="M36 10h3l4-3v10l-4-3h-3z" fill="#aaa"/>
  </svg>
  <span style="position:absolute;left:56px;top:8px"><b style="color:#fff;font-weight:400">0:02</b> / 4:17</span>
</div>

<div class="abs bar" style="left:111px;top:654px;width:350px">We strive to provide you with a wide range of treatment options:</div>
<div class="treat" style="left:112px;top:693px"><svg width="18" height="18"><circle cx="9" cy="9" r="8" fill="none" stroke="#2a66b5" stroke-width="1.5"/><path d="M5.5 6c0-1.5 1.5-2 3.5-1.3C11 4 12.5 4.5 12.5 6c0 2-1 3-1.3 6.5-.9 0-1.1-3-2.2-3s-1.3 3-2.2 3C6.5 9 5.5 8 5.5 6z" fill="#2a66b5"/></svg><span>General Dentistry</span></div>
<div class="treat" style="left:238px;top:693px"><svg width="18" height="18"><circle cx="9" cy="9" r="8" fill="none" stroke="#2a66b5" stroke-width="1.5"/><path d="M5.5 6c0-1.5 1.5-2 3.5-1.3C11 4 12.5 4.5 12.5 6c0 2-1 3-1.3 6.5-.9 0-1.1-3-2.2-3s-1.3 3-2.2 3C6.5 9 5.5 8 5.5 6z" fill="#2a66b5"/></svg><span>General Dentistry</span></div>
<div class="treat" style="left:357px;top:693px"><svg width="18" height="18"><circle cx="9" cy="9" r="8" fill="none" stroke="#2a66b5" stroke-width="1.5"/><path d="M5.5 6c0-1.5 1.5-2 3.5-1.3C11 4 12.5 4.5 12.5 6c0 2-1 3-1.3 6.5-.9 0-1.1-3-2.2-3s-1.3 3-2.2 3C6.5 9 5.5 8 5.5 6z" fill="#2a66b5"/></svg><span>General Dentistry</span></div>
<div class="treat" style="left:112px;top:720px"><svg width="18" height="18"><circle cx="9" cy="9" r="8" fill="none" stroke="#2a66b5" stroke-width="1.5"/><path d="M5.5 6c0-1.5 1.5-2 3.5-1.3C11 4 12.5 4.5 12.5 6c0 2-1 3-1.3 6.5-.9 0-1.1-3-2.2-3s-1.3 3-2.2 3C6.5 9 5.5 8 5.5 6z" fill="#2a66b5"/></svg><span>General Dentistry</span></div>
<div class="treat" style="left:238px;top:720px"><svg width="18" height="18"><circle cx="9" cy="9" r="8" fill="none" stroke="#2a66b5" stroke-width="1.5"/><path d="M5.5 6c0-1.5 1.5-2 3.5-1.3C11 4 12.5 4.5 12.5 6c0 2-1 3-1.3 6.5-.9 0-1.1-3-2.2-3s-1.3 3-2.2 3C6.5 9 5.5 8 5.5 6z" fill="#2a66b5"/></svg><span>General Dentistry</span></div>
<div class="treat" style="left:357px;top:720px"><svg width="18" height="18"><circle cx="9" cy="9" r="8" fill="none" stroke="#2a66b5" stroke-width="1.5"/><path d="M5.5 6c0-1.5 1.5-2 3.5-1.3C11 4 12.5 4.5 12.5 6c0 2-1 3-1.3 6.5-.9 0-1.1-3-2.2-3s-1.3 3-2.2 3C6.5 9 5.5 8 5.5 6z" fill="#2a66b5"/></svg><span>General Dentistry</span></div>
<div class="treat" style="left:112px;top:747px"><svg width="18" height="18"><circle cx="9" cy="9" r="8" fill="none" stroke="#2a66b5" stroke-width="1.5"/><path d="M5.5 6c0-1.5 1.5-2 3.5-1.3C11 4 12.5 4.5 12.5 6c0 2-1 3-1.3 6.5-.9 0-1.1-3-2.2-3s-1.3 3-2.2 3C6.5 9 5.5 8 5.5 6z" fill="#2a66b5"/></svg><span>General Dentistry</span></div>
<div class="treat" style="left:238px;top:747px"><svg width="18" height="18"><circle cx="9" cy="9" r="8" fill="none" stroke="#2a66b5" stroke-width="1.5"/><path d="M5.5 6c0-1.5 1.5-2 3.5-1.3C11 4 12.5 4.5 12.5 6c0 2-1 3-1.3 6.5-.9 0-1.1-3-2.2-3s-1.3 3-2.2 3C6.5 9 5.5 8 5.5 6z" fill="#2a66b5"/></svg><span>General Dentistry</span></div>
<div class="treat" style="left:357px;top:747px"><svg width="18" height="18"><circle cx="9" cy="9" r="8" fill="none" stroke="#2a66b5" stroke-width="1.5"/><path d="M5.5 6c0-1.5 1.5-2 3.5-1.3C11 4 12.5 4.5 12.5 6c0 2-1 3-1.3 6.5-.9 0-1.1-3-2.2-3s-1.3 3-2.2 3C6.5 9 5.5 8 5.5 6z" fill="#2a66b5"/></svg><span>General Dentistry</span></div>
<div class="abs link" style="left:111px;top:782px">View All Services</div>

<div class="abs bar" style="left:476px;top:654px;width:247px">Patient Case Studies</div>
<div class="abs thumb" style="left:476px;top:694px" role="img" aria-label="Smile close-up"></div>
<div class="abs case" style="left:528px;top:698px">Case Study #1:<br><b>Overbite</b></div>
<div class="abs thumb" style="left:606px;top:694px" role="img" aria-label="Smile close-up"></div>
<div class="abs case" style="left:659px;top:698px">Case Study #1:<br><b>Overbite</b></div>
<div class="abs thumb" style="left:476px;top:754px" role="img" aria-label="Smile close-up"></div>
<div class="abs case" style="left:528px;top:757px">Case Study #1:<br><b>Overbite</b></div>
<div class="abs thumb" style="left:606px;top:754px" role="img" aria-label="Smile close-up"></div>
<div class="abs case" style="left:659px;top:757px">Case Study #1:<br><b>Overbite</b></div>

<div class="abs social-box">
  <div class="fans"><i></i><b>Owen Hartley</b>, <b>Lena Voss</b> and 2,904,577 others like this.</div>
  <div class="follow">Follow Us on Friendbook</div>
  <div class="avatar" style="left:13px" role="img" aria-label="Follower photo"></div>
  <div class="avatar" style="left:48px" role="img" aria-label="Follower photo"></div>
  <div class="avatar" style="left:83px" role="img" aria-label="Follower photo"></div>
  <div class="avatar" style="left:117px" role="img" aria-label="Follower photo"></div>
  <div class="avatar" style="left:152px" role="img" aria-label="Follower photo"></div>
  <div class="avatar" style="left:186px" role="img" aria-label="Follower photo"></div>
  <div class="avatar" style="left:221px" role="img" aria-label="Follower photo"></div>
  <div class="avatar" style="left:255px" role="img" aria-label="Follower photo"></div>
  <div class="avatar" style="left:290px" role="img" aria-label="Follower photo"></div>
  <div class="avatar" style="left:324px" role="img" aria-label="Follower photo"></div>
  <div class="avatar" style="left:359px" role="img" aria-label="Follower photo"></div>
  <div class="avatar" style="left:393px" role="img" aria-label="Follower photo"></div>
  <div class="avatar" style="left:428px" role="img" aria-label="Follower photo"></div>
  <div class="avatar" style="left:462px" role="img" aria-label="Follower photo"></div>
  <div class="avatar" style="left:497px" role="img" aria-label="Follower photo"></div>
  <div class="avatar" style="left:531px" role="img" aria-label="Follower photo"></div>
  <div class="avatar" style="left:566px" role="img" aria-label="Follower photo"></div>
</div>

<footer class="abs footer">
  <h2 style="left:106px">Contact Info and Hours</h2>
  <h2 style="left:321px">Address &amp; Direction</h2>
  <h2 style="left:528px">Sign up for our Newsletter</h2>
</footer>
<div class="row" style="top:957px"><span>Phone</span><span>(905) 555.0167</span></div>
<div class="row" style="top:987px"><span>Fax</span><span>(905)555.0168</span></div>
<div class="row last" style="top:1016px;text-decoration:underline"><span>Email Us</span><span>Request Appointment</span></div>
<div class="row" style="top:1066px"><span>Monday - Friday</span><span>8:00 am - Late</span></div>
<div class="row" style="top:1095px"><span>Saturday</span><span>8:00 am - 12:00 pm</span></div>
<div class="row last" style="top:1124px"><span>Sunday</span><span>Closed</span></div>

<div class="addr" style="top:957px;font-weight:700">Merrow Dental</div>
<div class="addr" style="top:976px">1234 Your Street</div>
<div class="addr" style="top:996px">Your City, Country</div>
<div class="addr" style="top:1015px">(Free Parking at the Front)</div>
<div class="abs map" role="img" aria-label="Street map showing the office location"></div>

<div class="abs tips">To receive free dental tips from Dr. Calvin Merrow</div>
<div class="input" style="top:982px">Name</div>
<div class="input" style="top:1022px">Email</div>
<div class="input" style="top:1066px">Mobile Phone</div>
<div class="abs btn signup">Sign Up</div>

<div class="abs bottom">
  <i style="left:104px"></i><i style="left:136px"></i><i style="left:167px"></i><i style="left:197px"></i>
  <div class="copy">Copyright 2014 Dental Site &nbsp;|&nbsp; All Rights Reserved &nbsp;|&nbsp; Privacy Policy &nbsp;|&nbsp; Site Map</div>
</div>
</body>
</html>
```